Ridgeway Construction Letterhead

Looking for a new professional letter head for our business with one of the two logos on it. It must include all of the information listed below. The company is a heavy construction company and should have something strong looking to go along with the business. Needs to include all of the information we have listed, with nothing added. Looking for something that represents our business well. Would like it to be clean looking with nothing too fancy or colorful. Needs to be bold and strong.

Industry/Entity Type

Construction Company

Font styles to use
Sans Serif

Requirements
Must have
• One of the two logos attached
• Address - 718 Marrow Rd, Niagara on the Lake, ON L2K 4P8
• Phone Number - 905-614-3387
• Fax Number - 905-614-3392
• Website - www.ridgewayconstruction.ca
Nice to have
• Something clean and professional looking
Should not have
• Should not have the words "address", "phone number", etc.
• Only wrote those to have that info included

```html
<!DOCTYPE html>
<html lang="en">
<head>
<meta charset="utf-8">
<title>Ridgeway Construction Stationery</title>
<link href="https://fonts.googleapis.com/css2?family=Roboto:wght@400;500;700&family=Roboto+Condensed:wght@400;700&display=swap" rel="stylesheet">
<style>
  :root {
    --stage: #b3b3b3;
    --paper: #f7f7f5;
    --ink: #0b0b0b;
    --gold: #98742f;
    --text: #5a5a5a;
    --white: #ffffff;
    --slate: #3d3f41;
  }
  * { margin: 0; padding: 0; box-sizing: border-box; }
  html, body { width: 1200px; height: 1075px; overflow: hidden; }
  body { background: var(--stage); font-family: "Roboto", sans-serif; position: relative; }

  .letterhead { position: absolute; left: 109px; top: 67px; width: 665px; height: 939px; background: var(--paper); }
  .letterhead__header { position: absolute; left: 0; top: 0; width: 100%; height: 113px; background: var(--ink); }
  .letterhead__footer { position: absolute; left: 0; bottom: 0; width: 100%; height: 9px; background: var(--gold); }

  .brand { position: absolute; display: flex; align-items: center; gap: 9px; }
  .brand__mark { background: var(--gold); flex: none; }
  .brand__name { font-family: "Roboto Condensed", sans-serif; font-weight: 700; color: var(--white); text-transform: uppercase; line-height: 1.02; }

  .letterhead .brand { left: 42px; top: 29px; }
  .letterhead .brand__mark { width: 55px; height: 54px; }
  .letterhead .brand__name { font-size: 25px; letter-spacing: 0.3px; }

  .contact { position: absolute; right: 58px; top: 33px; color: var(--white); font-size: 11.5px; line-height: 14.8px; text-align: right; }
  .contact__row { position: relative; white-space: nowrap; }
  .contact__row svg { position: absolute; right: -17px; top: 2px; width: 10px; height: 10px; fill: var(--gold); }
  .contact__inline { position: relative; margin-right: 18px; }
  .contact__inline svg { position: absolute; right: -14px; top: 2px; width: 10px; height: 10px; fill: var(--gold); }

  .letter { position: absolute; left: 42px; top: 167px; width: 581px; color: var(--text); font-size: 11.4px; line-height: 15.2px; }
  .letter__date { margin-bottom: 30px; }
  .letter__recipient { margin-bottom: 30px; }
  .letter__recipient strong { font-weight: 500; }
  .letter__greeting { margin-bottom: 15px; }
  .letter p.body { text-align: justify; margin-bottom: 15px; }
  .signoff { position: absolute; left: 42px; top: 680px; color: var(--text); font-size: 11.4px; }
  .signoff__name { font-weight: 500; }
  .signoff__signature { width: 152px; height: 34px; margin: 8px 0 10px 0; background: linear-gradient(90deg, #dfe3ea, #eceff3); border-radius: 3px; }

  .card { position: absolute; left: 802px; width: 288px; height: 174px; background: var(--ink); overflow: hidden; }
  .card--front { top: 230px; }
  .card--back { top: 424px; }
  .card--front .brand { left: 44px; top: 62px; }
  .card--front .brand__mark { width: 47px; height: 47px; }
  .card--front .brand__name { font-size: 20.5px; }

  .card__id { position: absolute; left: 27px; top: 32px; width: 96px; display: flex; flex-direction: column; align-items: center; gap: 8px; }
  .card__id .brand__mark { width: 58px; height: 57px; }
  .card__id .brand__name { font-size: 14px; text-align: center; }

  .card__person { position: absolute; left: 155px; top: 41px; }
  .card__name { font-family: "Roboto Condensed", sans-serif; color: var(--gold); font-size: 12px; text-transform: uppercase; }
  .card__role { color: var(--white); font-size: 7px; margin-top: 3px; }
  .card__details { position: absolute; left: 155px; top: 77px; color: var(--white); font-size: 7px; line-height: 10.2px; list-style: none; }
  .card__details li { position: relative; padding-left: 13px; }
  .card__details svg { position: absolute; left: 0; top: 2px; width: 6.5px; height: 6.5px; fill: var(--gold); }
  .card__strip { position: absolute; left: 0; bottom: 0; width: 100%; height: 22px; }
  .card__web { position: absolute; left: 155px; bottom: 7px; color: var(--white); font-size: 7px; }
</style>
</head>
<body>

<svg width="0" height="0" style="position:absolute">
  <defs>
    <symbol id="icon-phone" viewBox="0 0 20 20"><path d="M2 7c0-3 3-5 8-5s8 2 8 5l-4 1-1-2H7L6 8zM5 10l2-2h6l2 2v7H5z"/></symbol>
    <symbol id="icon-fax" viewBox="0 0 20 20"><path d="M5 1h10v5H5zM2 7h16v8h-3v4H5v-4H2zm5 6v4h6v-4z"/></symbol>
    <symbol id="icon-web" viewBox="0 0 20 20"><path d="M10 1a9 9 0 100 18 9 9 0 000-18zm0 2c1 1 2 3 2 6H8c0-3 1-5 2-6zM3 11h3c0 2 1 4 2 5a7 7 0 01-5-5zm0-2a7 7 0 015-5C7 5 6 7 6 9zm5 2h4c0 2-1 4-2 5-1-1-2-3-2-5zm6 0h3a7 7 0 01-5 5c1-1 2-3 2-5zm0-2c0-2-1-4-2-5a7 7 0 015 5z"/></symbol>
    <symbol id="icon-pin" viewBox="0 0 20 20"><path d="M10 1a6 6 0 00-6 6c0 5 6 12 6 12s6-7 6-12a6 6 0 00-6-6zm0 8.5A2.5 2.5 0 1110 4.5a2.5 2.5 0 010 5z"/></symbol>
  </defs>
</svg>

<main class="letterhead">
  <header class="letterhead__header">
    <div class="brand">
      <span class="brand__mark"></span>
      <span class="brand__name">Ridgeway<br>Construction</span>
    </div>
    <address class="contact" style="font-style:normal">
      <div class="contact__row"><span class="contact__inline">905-614-3387<svg><use href="#icon-phone"/></svg></span>905-614-3392<svg><use href="#icon-fax"/></svg></div>
      <div class="contact__row">www.ridgewayconstruction.ca<svg><use href="#icon-web"/></svg></div>
      <div class="contact__row">718 Marrow Rd, Niagara<svg><use href="#icon-pin"/></svg></div>
      <div class="contact__row">on the Lake, ON L2K 4P8</div>
    </address>
  </header>

  <section class="letter">
    <p class="letter__date">30/20/2016</p>
    <p class="letter__recipient"><strong>Mr. XYZ Smith</strong><br>123, Street No. 123,<br>City Name<br>Pincode-123456</p>
    <p class="letter__greeting">Dear Sir,</p>
    <p class="body">Lorem Ipsum is simply dummy text of the printing and typesetting industry. Lorem Ipsum has been the industry's standard dummy text ever since the 1500s, when an unknown printer took a galley of type and scrambled it to make a type specimen book. It has survived not only five centuries, but also the leap into electronic typesetting, remaining essentially unchanged. It was popularised in the 1960s with the release of Tessel sheets containing Lorem Ipsum passages, and more recently with desktop publishing software like Lumen Layout including versions of Lorem Ipsum.</p>
    <p class="body">Lorem Ipsum is simply dummy text of the printing and typesetting industry. Lorem Ipsum has been the industry's standard dummy text ever since the 1500s, when an unknown printer took a galley of type and scrambled it to make a type specimen book. It has survived not only five centuries, but also the leap into electronic typesetting, remaining essentially unchanged. It was popularised in the 1960s with the release of Tessel sheets containing Lorem Ipsum passages, and more recently with desktop publishing software like Lumen Layout including versions of Lorem Ipsum.</p>
    <p class="body">Lorem Ipsum is simply dummy text of the printing and typesetting industry. Lorem Ipsum has been the industry's standard dummy text ever since the 1500s, when an unknown printer took a galley of type and scrambled it to make a type specimen book.</p>
    <p class="body">Lorem Ipsum is simply dummy text of the printing and typesetting industry. Lorem Ipsum has been the industry's standard dummy text ever since the 1500s, when an unknown printer took a galley of type and scrambled it to make a type specimen book.</p>
  </section>

  <section class="signoff">
    <p class="signoff__name">Your Name</p>
    <div class="signoff__signature" role="img" aria-label="Handwritten signature"></div>
    <p>CEO &nbsp;|&nbsp; Owner</p>
  </section>

  <footer class="letterhead__footer"></footer>
</main>

<section class="card card--front">
  <div class="brand">
    <span class="brand__mark"></span>
    <span class="brand__name">Ridgeway<br>Construction</span>
  </div>
</section>

<section class="card card--back">
  <div class="card__id brand">
    <span class="brand__mark"></span>
    <span class="brand__name">Ridgeway<br>Construction</span>
  </div>
  <div class="card__person">
    <p class="card__name">John Doe John</p>
    <p class="card__role">Managing Partner</p>
  </div>
  <ul class="card__details">
    <li><svg><use href="#icon-phone"/></svg>905-614-3387</li>
    <li><svg><use href="#icon-fax"/></svg>905-614-3392</li>
    <li><svg><use href="#icon-pin"/></svg>718 Marrow Rd, Niagara<br>on the Lake, ON L2K 4P8</li>
  </ul>
  <svg class="card__strip" viewBox="0 0 288 22" preserveAspectRatio="none">
    <rect x="0" y="16" width="288" height="6" fill="var(--gold)"/>
    <polygon points="140,0 288,0 288,22 130,22" fill="var(--slate)"/>
  </svg>
  <p class="card__web">www.ridgewayconstruction.ca</p>
</section>

</body>
</html>
```